Colwyn Marsh Optometry 10 Year Celebration

Front of invitation
Size 107-139mm
Font – Georgia
The invitation should be worded as follows;
Colwyn Marsh Optometry
would like to invite you to...

```html
<!DOCTYPE html>
<html lang="en">
<head>
<meta charset="utf-8">
<title>Colwyn Marsh Optometry – 10 Year Celebration Invitation</title>
<link href="https://fonts.googleapis.com/css2?family=Gelasio:wght@400;700&family=Yellowtail&display=block" rel="stylesheet">
<style>
  :root {
    --plum: #55325a;
    --plum-deep: #3a2340;
    --gold: #f2d46a;
    --gold-rich: #d9b23a;
    --white: #ffffff;
    --stage: #05070f;
    --ink: #2e1f33;
  }
  * { box-sizing: border-box; margin: 0; padding: 0; }
  html, body { width: 1200px; height: 709px; overflow: hidden; background: var(--stage); }
  body { font-family: "Gelasio", Georgia, serif; position: relative; }

  .card { position: absolute; left: 280px; width: 640px; height: 320px; overflow: hidden; }
  .card--front { top: 22px; }
  .card--back { top: 367px; background: var(--white); }

  /* Front */
  .stripes {
    position: absolute; inset: 0;
    background: repeating-linear-gradient(to bottom,
      var(--plum) 0 64px, var(--white) 64px 128px);
  }
  .confetti-haze {
    position: absolute; left: 60px; top: 0; width: 560px; height: 320px;
    background: radial-gradient(ellipse 48% 50% at 50% 50%,
      rgba(242, 212, 106, 0.75) 0%, rgba(217, 178, 58, 0.45) 45%, rgba(217, 178, 58, 0) 100%);
  }
  .seal {
    position: absolute; left: 208px; top: 24px; width: 262px; height: 262px;
    border-radius: 50%; background: var(--gold);
    box-shadow: 0 4px 10px rgba(0,0,0,0.25);
  }
  .seal-text { position: absolute; left: 0; width: 100%; text-align: center; color: var(--ink); line-height: 1; white-space: nowrap; }
  .seal-host { top: 36px; font-weight: 700; font-size: 14px; }
  .seal-invite { top: 51px; font-size: 12px; }
  .seal-occasion { top: 176px; font-size: 14.5px; }
  .seal-location { top: 193px; font-size: 18px; }
  .seal-details { top: 214px; font-size: 10px; line-height: 12px; }

  .headline {
    position: absolute; left: 100px; top: 92px; width: 450px; height: 100px;
    font-family: "Yellowtail", "Brush Script MT", cursive; font-weight: 400;
    font-size: 108px; line-height: 100px; white-space: nowrap;
    color: var(--plum); text-align: center; letter-spacing: -1px;
    -webkit-text-stroke: 9px var(--white); paint-order: stroke fill;
    text-shadow: 0 3px 6px rgba(0,0,0,0.25);
  }
  .wordmark {
    position: absolute; display: flex; align-items: center; gap: 6px;
    font-size: 12px; line-height: 1; white-space: nowrap;
  }
  .wordmark-dot { width: 8px; height: 8px; border-radius: 50%; }
  .card--front .wordmark { right: 20px; bottom: 22px; color: var(--white); }
  .card--front .wordmark-dot { background: var(--white); }

  /* Back */
  .back-fade {
    position: absolute; left: 0; top: 0; width: 100%; height: 150px;
    background: linear-gradient(to bottom, var(--plum) 0%, rgba(85,50,90,0.55) 35%, rgba(255,255,255,0) 100%);
  }
  .back-confetti {
    position: absolute; left: 0; top: 0; width: 100%; height: 220px;
    background: radial-gradient(ellipse 60% 55% at 50% 20%, rgba(242,212,106,0.28), rgba(242,212,106,0) 100%);
  }
  .gold-rule { position: absolute; left: 0; width: 100%; height: 3px; background: var(--gold-rich); }
  .gold-rule--top { top: 0; }
  .gold-rule--bottom { top: 273px; }
  .back-heading {
    position: absolute; top: 54px; width: 100%; text-align: center;
    font-weight: 700; font-size: 23px; line-height: 24px; color: var(--ink);
  }
  .back-body {
    position: absolute; top: 122px; width: 100%; text-align: center;
    font-size: 11.5px; line-height: 15.5px; color: var(--ink);
  }
  .back-body p + p { margin-top: 16px; }
  .card--back .wordmark { left: 50%; top: 242px; transform: translateX(-50%); color: var(--ink); font-size: 13px; }
  .card--back .wordmark-dot { background: var(--ink); }
  .footer-band {
    position: absolute; left: 0; bottom: 0; width: 100%; height: 44px;
    background: var(--plum); color: var(--white);
    display: flex; align-items: center; justify-content: center; gap: 8px;
    font-size: 11.5px;
  }
  .footer-item { display: flex; align-items: center; gap: 4px; }
  .footer-icon { width: 9px; height: 10px; fill: var(--white); }
</style>
</head>
<body>

<section class="card card--front" aria-label="Invitation front">
  <div class="stripes"></div>
  <div class="confetti-haze" role="img" aria-label="Gold confetti scattered around the anniversary seal"></div>
  <div class="seal">
    <p class="seal-text seal-host">Colwyn Marsh Optometry</p>
    <p class="seal-text seal-invite">would like to invite you to help us</p>
    <p class="seal-text seal-occasion">our 10 year anniversary!</p>
    <p class="seal-text seal-location">In our new location</p>
    <p class="seal-text seal-details">24 Kestrel Lane Harwood NSW<br>Tuesday 12th December<br>11:00 am – 7:00 pm</p>
  </div>
  <h1 class="headline">Celebrate</h1>
  <div class="wordmark"><span class="wordmark-dot"></span>Colwyn Marsh Optometry</div>
</section>

<section class="card card--back" aria-label="Invitation back">
  <div class="back-fade"></div>
  <div class="back-confetti" role="img" aria-label="Falling gold confetti and streamers"></div>
  <div class="gold-rule gold-rule--top"></div>
  <h2 class="back-heading">You are personally invited to come and<br>experience our brand new store!</h2>
  <div class="back-body">
    <p>Be one of the first to come in, with a chance to try some new frames!<br>
    Special guests include a colour consultant &amp; brand representatives. Refreshments &amp; nibbles provided.<br>
    Champagne into the evening.</p>
    <p>We would love the opportunity to celebrate with our local community<br>
    so bring along your friends &amp; family!</p>
  </div>
  <div class="wordmark"><span class="wordmark-dot"></span>Colwyn Marsh Optometry</div>
  <div class="gold-rule gold-rule--bottom"></div>
  <footer class="footer-band">
    <span class="footer-item">
      <svg class="footer-icon" viewBox="0 0 10 12" aria-hidden="true"><path d="M5 0a4 4 0 0 0-4 4c0 3 4 8 4 8s4-5 4-8a4 4 0 0 0-4-4zm0 5.6A1.6 1.6 0 1 1 5 2.4a1.6 1.6 0 0 1 0 3.2z"/></svg>
      24 Kestrel Lane Harwood NSW
    </span>
    <span>|</span>
    <span class="footer-item">
      <svg class="footer-icon" viewBox="0 0 12 12" aria-hidden="true"><path d="M2.5 0.5l2 2.2-1 1.4c.8 1.6 2 2.8 3.6 3.6l1.4-1 2.2 2-1.2 2.3C4.8 10.6 1.4 7.2.3 1.7z"/></svg>
      (02) 5550 1847
    </span>
  </footer>
</section>

</body>
</html>
```